VERIDAX Need a luxury modern business card designed.

Need a luxury modern business card designed. refer to the uploaded files for the company name and logo in the zip file under source files. i will making my descion on monday. so please send in before then so if we need to edit we will have the time. we have a trade show coming up and im on a deadline for printer.

Target Market(s)

high end clients

Contact Information for Business Card

Company nAme and logo. Calvin Ostrow Co-Founder / Project Manager Office # 416-555-0193 Cell # 416-555-0147 VERIDAX.CA Calvin@veridax.ca

Font styles to use
Other font styles liked:
• Modern

Requirements
Must have
• Company name and logo, contact info, using the black, gold and white color scheme.

```html
<!DOCTYPE html>
<html lang="en">
<head>
<meta charset="utf-8">
<title>VERIDAX Business Card</title>
<link href="https://fonts.googleapis.com/css2?family=Lato:wght@300;400;900&display=swap" rel="stylesheet">
<style>
  :root {
    --stage: #e6e6e4;
    --ink: #2b2b2b;
    --charcoal: #333333;
    --gold: #a8976a;
    --paper: #ffffff;
    --rule: #9a9a9a;
  }
  * { margin: 0; padding: 0; box-sizing: border-box; }
  html, body { width: 1200px; height: 900px; overflow: hidden; }
  body {
    background: var(--stage);
    font-family: "Lato", sans-serif;
    position: relative;
  }
  .card {
    position: absolute;
    left: 250px;
    width: 700px;
    height: 400px;
    border-radius: 22px;
    overflow: hidden;
    box-shadow: 0 10px 28px rgba(0,0,0,0.18);
  }
  .card-back { top: 30px; background: var(--charcoal); }
  .card-back .pattern-field {
    position: absolute; inset: 0;
    background: linear-gradient(135deg, #363636 0%, #2f2f2f 100%);
  }
  .card-back .back-name {
    position: absolute; right: 70px; top: 150px;
    font-weight: 300; font-size: 22px; letter-spacing: 6px;
    color: var(--gold);
  }
  .card-front { top: 470px; background: var(--paper); }
  .swoosh { position: absolute; inset: 0; }
  .brand {
    position: absolute; left: 60px; top: 165px;
    display: flex; align-items: center; gap: 14px;
  }
  .brand-mark { width: 16px; height: 16px; background: var(--gold); }
  .brand-name {
    font-weight: 300; font-size: 44px; letter-spacing: 7px;
    color: var(--ink);
  }
  .divider {
    position: absolute; left: 350px; top: 95px;
    width: 1px; height: 150px; background: var(--rule);
  }
  .contact { position: absolute; left: 385px; top: 60px; }
  .person-name {
    font-weight: 900; font-size: 30px; color: var(--gold); line-height: 1;
  }
  .person-role {
    font-weight: 400; font-size: 17px; color: var(--ink); margin-top: 4px;
  }
  .contact-list { list-style: none; margin-top: 18px; }
  .contact-list li {
    display: flex; align-items: center; gap: 12px;
    font-size: 17px; color: var(--ink); height: 27px;
  }
  .contact-list svg { width: 15px; height: 15px; fill: var(--gold); flex: none; }
</style>
</head>
<body>

<section class="card card-back">
  <div class="pattern-field" role="img" aria-label="Repeating faint brand-mark pattern in dark grey and muted gold"></div>
  <span class="back-name">VERIDAX</span>
</section>

<section class="card card-front">
  <svg class="swoosh" viewBox="0 0 700 400" preserveAspectRatio="none" aria-hidden="true">
    <path d="M0 330 Q 360 300 700 200 L700 400 L0 400 Z" fill="#333333"/>
    <path d="M380 345 Q 560 300 700 196" fill="none" stroke="#ffffff" stroke-width="10"/>
    <path d="M360 350 Q 560 305 700 192" fill="none" stroke="#a8976a" stroke-width="5"/>
  </svg>

  <div class="brand">
    <span class="brand-mark"></span>
    <span class="brand-name">VERIDAX</span>
  </div>

  <div class="divider"></div>

  <div class="contact">
    <div class="person-name">Calvin Ostrow</div>
    <div class="person-role">Co-Founder</div>
    <ul class="contact-list">
      <li>
        <svg viewBox="0 0 16 16"><path d="M2 5c0-2 2-3 6-3s6 1 6 3v1h-3V5H5v1H2zM4 7h8l2 6H2z"/></svg>
        416-555-0193
      </li>
      <li>
        <svg viewBox="0 0 16 16"><path d="M4 1h8v14H4zM5.5 2.5v9h5v-9zM7 12.5h2v1H7z" fill-rule="evenodd"/></svg>
        416-555-0147
      </li>
      <li>
        <svg viewBox="0 0 16 16"><path d="M1 3h14v10H1zM2 4l6 5 6-5z" fill-rule="evenodd"/></svg>
        Calvin@veridax.ca
      </li>
      <li>
        <svg viewBox="0 0 16 16"><circle cx="8" cy="8" r="7"/><path d="M1 8h14M8 1v14M3 4h10M3 12h10" stroke="#fff" stroke-width="0.8" fill="none"/></svg>
        www.veridax.ca
      </li>
    </ul>
  </div>
</section>

</body>
</html>
```